Flyer Template Design

I have attached 4 files. I would like a design template that could be used across these documents so that they have a common look and feel. The content of the documents is tested and should not be changed significantly. The images can be changed. I have also attache our logo for color compatibility.
Updates

Need extra days to review

Target Market(s)

Wealthy Christian donors

Font styles to use
Serif
Sans Serif

```html
<!DOCTYPE html>
<html lang="en">
<head>
<meta charset="utf-8">
<title>God's Heart for the Nations – Flyer</title>
<link rel="stylesheet" href="https://fonts.googleapis.com/css2?family=Noto+Sans:wght@400;500&family=Source+Sans+3:wght@400;600;700&display=swap">
<style>
:root{
  --page-bg:#dcdcdc;
  --paper:#ffffff;
  --cyan:#00c8f0;
  --cyan-light:#7fe3f8;
  --wave-blue:#0b5fa3;
  --sky-top:#ffffff;
  --sky-bottom:#9fd2ee;
  --green:#2e9b4f;
  --ink:#1b1b1b;
  --photo-warm:#8a4a2c;
  --photo-cool:#2f8fc2;
}
*{box-sizing:border-box;margin:0;padding:0}
html,body{width:1108px;height:1200px;overflow:hidden;background:var(--page-bg)}
.flyer{position:absolute;left:117px;top:0;width:873px;height:1200px;background:var(--paper);overflow:hidden;
  font-family:"Source Sans 3",sans-serif;color:var(--ink);font-size:15px;line-height:18px}
.header{position:absolute;left:0;top:0;width:873px;height:175px}
.header svg{position:absolute;left:0;top:0}
.title{position:absolute;left:40px;top:32px;font-family:"Noto Sans",sans-serif;font-weight:400;font-size:44px;line-height:56px;color:#0a1a24;letter-spacing:-0.3px}
.sky{position:absolute;left:0;top:450px;width:873px;height:560px;
  background:linear-gradient(180deg,var(--sky-top) 0%,#e4f2fb 25%,#c2e2f4 60%,var(--sky-bottom) 100%)}
.photo-strip{position:absolute;left:0;top:156px;width:517px;height:308px;
  background:linear-gradient(90deg,#3a2a22 0%,var(--photo-warm) 35%,#b5342c 55%,#7a3a4a 75%,#4a3428 100%)}
.intro{position:absolute;left:539px;top:154px;width:300px}
.intro p{margin-bottom:18px}
.body{position:absolute;left:41px;top:480px;width:800px}
.body p{margin-bottom:18px}
.section-title{font-family:"Noto Sans",sans-serif;font-weight:400;font-size:29px;line-height:34px;margin:-1px 0 12px}
.task p{font-size:14.5px;line-height:17.3px}
.cta-lead{font-weight:600;font-size:19px;line-height:22px;margin:-6px 0 6px !important}
.join{font-weight:600;font-size:14.5px;margin-bottom:10px !important}
.contact{font-weight:600;font-size:14.5px}
.footer-wave{position:absolute;left:0;top:960px}
.brand{position:absolute;left:48px;top:1040px;display:flex;align-items:center;gap:16px}
.brand-square{width:62px;height:62px;background:var(--cyan)}
.brand-name{font-family:"Source Sans 3",sans-serif;font-weight:400;font-size:28px;line-height:28px;color:#1b1b1b;letter-spacing:0.5px}
.people-strip{position:absolute;left:357px;top:1008px;width:516px;height:150px;
  background:linear-gradient(90deg,var(--photo-cool) 0%,#d6a431 22%,#cfc8bd 40%,#3b2e2c 58%,#b9a189 78%,#c98a2a 100%)}
</style>
</head>
<body>
<main class="flyer">
  <div class="sky"></div>
  <header class="header">
    <svg width="873" height="175" viewBox="0 0 873 175" aria-hidden="true">
      <defs>
        <linearGradient id="headGrad" x1="0" y1="0" x2="0" y2="1">
          <stop offset="0" stop-color="var(--cyan)"/>
          <stop offset="1" stop-color="var(--cyan-light)"/>
        </linearGradient>
      </defs>
      <path d="M0 0H873V150C760 120 640 100 480 118C320 136 160 138 0 112Z" fill="url(#headGrad)"/>
      <path d="M0 104C160 132 320 128 480 110C640 92 760 100 873 140V172C760 126 640 108 480 124C320 140 160 142 0 116Z" fill="var(--wave-blue)"/>
    </svg>
    <h1 class="title">God’s Heart for the Nations</h1>
  </header>

  <div class="photo-strip" role="img" aria-label="Row of five portraits of people from different nations in traditional dress"></div>

  <section class="intro">
    <p>From beginning to end, the Bible reveals God’s heart for “the nations.” In <b>Genesis</b>, God promises Abraham, “through your offspring all nations on the earth will be blessed.”</p>
    <p>The <b>Psalms</b> prophesy that “all the nations you have made will come and worship before you, Lord…” In <b>Isaiah</b>, God promises the Messiah, “I will make you a light to the nations, that my salvation may reach to the ends of the earth.”</p>
    <p><b>Daniel</b> sees “one like a son of man” who “was given authority, glory and sovereign power; all nations and peoples of every language worshiped him.”</p>
  </section>

  <section class="body">
    <p>In <b>Matthew</b>, Jesus commands his apostles to “Go and make disciples of all nations.” And he links his return to the completion of that task, saying, “This gospel of the kingdom will be preached in the whole world as a testimony to all nations, and then the end will come.”</p>
    <p>In <b>Revelation</b>, John sees a “great multitude that no one could number, from every nation, from all tribes and peoples and languages, standing before the throne…”</p>
    <p>In the Bible, the word “nations” refers to people groups: groups of people who share a common ethnicity, culture, and language. Amazingly, there are more than 12,000 of these nations scattered around the world—and God has promised that every one of them will be included in His Kingdom.</p>
    <div class="task">
      <h2 class="section-title">FINISHING THE TASK</h2>
      <p>Today, there are still 500 nations who are not yet represented in God’s Kingdom. No one has ever proclaimed the gospel to these “unengaged” people groups, and there are no believers among them. For these groups, God’s promises have yet to be fulfilled. Most of these groups are small and located in remote, difficult places. But because we now know who and where they are, by God’s grace it is possible that we can engage every one of them with the gospel within the next 3 years.</p>
      <p class="cta-lead">You can make that happen.</p>
      <p>Partner with the Harvest Fund and finance the missionaries who are taking the gospel for the first time to those last remaining people groups. Your investment will “hastening the coming of the day of God” by accelerating the effort to make “disciples in every nation.” In 2018, our partners helped take the gospel to 231 people groups in 35 countries.</p>
      <p class="join">Join us as we invest to make disciples in “all nations” by 2022.</p>
      <p class="contact">To learn more, email Dan Carter at dcarter@harvestfund.org.</p>
    </div>
  </section>

  <svg class="footer-wave" width="873" height="240" viewBox="0 0 873 240" aria-hidden="true">
    <path d="M0 30C140 60 300 42 480 24C640 8 760 10 873 20V240H0Z" fill="var(--paper)"/>
    <path d="M0 12C140 50 300 36 480 18C640 2 760 2 873 10V22C760 12 640 12 480 28C300 46 140 60 0 26Z" fill="var(--green)"/>
  </svg>

  <div class="brand">
    <div class="brand-square"></div>
    <div class="brand-name">THE<br>HARVEST<br>FUND</div>
  </div>

  <div class="people-strip" role="img" aria-label="Row of six smiling portraits of people from different cultures"></div>
</main>
</body>
</html>
```